Redesign a Start-Up Dating Website

Website: https://morvelink.com.
Make sure the design has an island style theme.
I would like the 7 pages of my website to have a new and professional look. I want the same colors to remain, but I want a creative look for all the pages. This is a dating website that is in the startup stage. So, I want to give my entire website a custom makeover. I want something that will stand out from the other dating sites. Something that will attract more people to want to use my services, and hopefully get new members.
Target Market(s)
Dating
Industry/Entity Type
Dating
Coding
Coded - Design and coding required
Number of Pages Required
5+ page
Font styles to use
Other font styles liked:
- Decorative, San Serif
Requirements
Must have
- The design must have the original colors and a stylish font to go along. The design must be creative, welcoming, and professional. I would like an island style theme for the website. This is a dating website so make sure that the design is tailored to that aspect.
Nice to have
- It would be nice to have a decorative font and a professional style on all the pages. Make sure the design will be mobile responsive and friendly for all the pages on the website.
Should not have
- The design should not be bland and uncreative.

```html
<!DOCTYPE html>
<html lang="en">
<head>
<meta charset="utf-8">
<title>Contact – Morvelink</title>
<link href="https://fonts.googleapis.com/css2?family=Raleway:wght@600;700;800&family=Open+Sans:wght@400;600;700&display=swap" rel="stylesheet">
<style>
:root{
  --orange:#f7941d;
  --teal:#34b8a3;
  --logo-teal:#5fb49c;
  --ink:#333333;
  --muted:#555555;
  --line:#8a8a8a;
  --footer-bg:#ececec;
  --white:#ffffff;
}
*{box-sizing:border-box;margin:0;padding:0}
html,body{width:1099px;height:1200px;overflow:hidden;background:var(--white)}
body{position:relative;font-family:"Open Sans",sans-serif;color:var(--ink)}
.abs{position:absolute}
.top-bar{left:0;top:0;width:1099px;height:3px;background:linear-gradient(90deg,var(--teal),var(--orange))}
.site-header{left:0;top:3px;width:1099px;height:81px;background:var(--white);box-shadow:0 2px 4px rgba(0,0,0,.12);z-index:2}
.brand{left:87px;top:14px;display:flex;align-items:center;gap:6px}
.brand-dot{width:52px;height:52px;border-radius:50%;background:var(--orange)}
.brand-name{font-family:"Raleway",sans-serif;font-weight:700;font-size:31px;color:var(--logo-teal)}
.main-nav{left:348px;top:32px;display:flex;gap:24px;font-family:"Raleway",sans-serif;font-weight:700;font-size:14px;text-transform:uppercase}
.main-nav a{color:var(--ink);text-decoration:none}
.main-nav a.is-active{color:var(--orange)}
.login-btn{left:915px;top:20px;width:94px;height:38px;border-radius:19px;background:var(--orange);color:var(--white);font-family:"Raleway",sans-serif;font-weight:700;font-size:14px;display:flex;align-items:center;justify-content:center;gap:6px}
.hero{left:0;top:84px;width:1099px;height:260px;background:linear-gradient(180deg,#6f7295 0%,#9a8fa8 35%,#c8a6a6 55%,#7b7f9d 68%,#3f4f78 100%)}
.hero-title{left:0;top:170px;width:1099px;text-align:center;font-family:"Raleway",sans-serif;font-weight:800;font-size:60px;color:var(--white);letter-spacing:1px}
.breadcrumb{left:90px;top:363px;font-family:"Raleway",sans-serif;font-weight:700;font-size:13px;display:flex;gap:10px}
.breadcrumb .current{color:var(--orange)}
.divider{left:90px;top:395px;width:919px;height:1px;background:var(--line)}
.form-intro{left:91px;top:476px;width:560px;font-weight:700;font-size:14.5px;line-height:28px;text-transform:uppercase;color:var(--ink)}
.field-label{font-size:12px;color:var(--muted)}
.field{border:1px solid #777;background:var(--white);height:29px}
.select-text{font-size:11px;color:var(--ink);padding:8px 11px}
.select-caret{right:0;top:0;width:31px;height:27px;border-left:1px solid #777;display:flex;align-items:center;justify-content:center}
.submit-btn{left:91px;top:858px;width:102px;height:38px;border-radius:19px;background:var(--orange);color:var(--white);font-weight:700;font-size:14px;display:flex;align-items:center;justify-content:center}
.info-card{left:688px;top:477px;width:320px;height:415px;background:var(--teal);color:var(--white)}
.info-title{left:26px;top:22px;font-family:"Raleway",sans-serif;font-weight:700;font-size:21px}
.info-text{left:30px;top:62px;width:270px;font-size:12px;line-height:22px}
.info-icon{width:39px;height:39px;border:1.5px solid var(--white);border-radius:50%;display:flex;align-items:center;justify-content:center}
.info-line{font-size:13px;line-height:22px}
.social{width:37px;height:37px;border:1.5px solid var(--white);border-radius:50%}
.site-footer{left:0;top:975px;width:1099px;height:225px;background:var(--footer-bg)}
.footer-bar{left:0;top:0;width:1099px;height:5px;background:linear-gradient(90deg,var(--teal),var(--orange))}
.footer-icon{width:40px;height:40px;border:1px solid #777;border-radius:50%;display:flex;align-items:center;justify-content:center}
.footer-text{font-size:13px;color:var(--muted);line-height:22px}
.footer-links{left:0;top:108px;width:1099px;text-align:center;font-size:13px;color:var(--muted);word-spacing:3px}
.footer-rule{left:90px;top:156px;width:919px;height:1px;background:#ccc}
.copyright{left:92px;top:180px;font-size:12px;color:var(--muted)}
.footer-social{width:34px;height:34px;border:1px solid #777;border-radius:50%}
</style>
</head>
<body>
<div class="abs top-bar"></div>
<header class="abs site-header">
  <div class="abs brand"><span class="brand-dot"></span><span class="brand-name">Morvelink</span></div>
  <nav class="abs main-nav">
    <a href="#">Home</a><a href="#">Search</a><a href="#">Members</a><a href="#">Extras</a><a href="#">About</a><a href="#">Premium</a><a href="#" class="is-active">Contact</a>
  </nav>
  <div class="abs login-btn">
    <svg width="10" height="12" viewBox="0 0 10 12"><rect x="0" y="5" width="10" height="7" rx="1" fill="#fff"/><path d="M2.5 5V3.5a2.5 2.5 0 0 1 5 0V5" stroke="#fff" stroke-width="1.6" fill="none"/></svg>LOGIN
  </div>
</header>

<div class="abs hero" role="img" aria-label="Photo of a couple holding hands on a beach at sunset"></div>
<h1 class="abs hero-title">CONTACT</h1>

<div class="abs breadcrumb"><span>HOME</span><span>&gt;&gt;</span><span class="current">CONTACT</span></div>
<div class="abs divider"></div>

<p class="abs form-intro">Fill out this form any time you need professional support or to just give your feedback and comments.</p>

<span class="abs field-label" style="left:94px;top:571px">Name/Username:*</span>
<div class="abs field" style="left:91px;top:591px;width:271px"></div>
<span class="abs field-label" style="left:372px;top:571px">Email :</span>
<div class="abs field" style="left:372px;top:591px;width:272px"></div>

<span class="abs field-label" style="left:91px;top:635px">Phone :</span>
<div class="abs field" style="left:91px;top:655px;width:271px"></div>
<span class="abs field-label" style="left:372px;top:635px">Issue type:</span>
<div class="abs field" style="left:372px;top:655px;width:272px">
  <div class="select-text">Account &amp; Billing</div>
  <div class="abs select-caret"><svg width="8" height="5" viewBox="0 0 8 5"><path d="M0 0h8L4 5z" fill="#333"/></svg></div>
</div>

<span class="abs field-label" style="left:91px;top:697px">Subject:*</span>
<div class="abs field" style="left:91px;top:718px;width:553px"></div>

<span class="abs field-label" style="left:91px;top:760px">Message:*</span>
<div class="abs field" style="left:91px;top:781px;width:553px;height:54px"></div>

<div class="abs submit-btn">SIGN UP</div>

<aside class="abs info-card">
  <h2 class="abs info-title">CONTACT INFORMATION</h2>
  <p class="abs info-text">At vero eos et accusamus et iusto odio dignimos ducimus qui blanditiis praesentium voluptatum deleniti atque corrupti quos.</p>

  <div class="abs info-icon" style="left:27px;top:159px"><svg width="12" height="17" viewBox="0 0 12 17"><path d="M6 0a6 6 0 0 0-6 6c0 4.5 6 11 6 11s6-6.5 6-11a6 6 0 0 0-6-6zm0 8.5A2.5 2.5 0 1 1 6 3.5a2.5 2.5 0 0 1 0 5z" fill="#fff"/></svg></div>
  <p class="abs info-line" style="left:84px;top:157px;width:200px">Coral Bay Road, Palm Isle, 00481</p>

  <div class="abs info-icon" style="left:27px;top:224px"><svg width="15" height="15" viewBox="0 0 16 16"><path d="M3.5 0.5l2.5 3-1.6 2a9 9 0 0 0 6.1 6.1l2-1.6 3 2.5-1.3 2.6C7.5 15 1 8.5.9 1.8z" fill="#fff"/></svg></div>
  <p class="abs info-line" style="left:84px;top:233px">1 555 204 7310</p>

  <div class="abs info-icon" style="left:27px;top:285px"><svg width="18" height="13" viewBox="0 0 18 13"><rect width="18" height="13" rx="1.5" fill="#fff"/><path d="M0.5 1.5l8.5 6 8.5-6" stroke="#34b8a3" stroke-width="1.5" fill="none"/></svg></div>
  <p class="abs info-line" style="left:84px;top:294px">contact@morvelink.com</p>

  <span class="abs social" style="left:27px;top:349px"></span>
  <span class="abs social" style="left:70px;top:349px"></span>
  <span class="abs social" style="left:112px;top:349px"></span>
</aside>

<footer class="abs site-footer">
  <div class="abs footer-bar"></div>
  <div class="abs footer-icon" style="left:210px;top:40px"><svg width="10" height="14" viewBox="0 0 12 17"><path d="M6 0a6 6 0 0 0-6 6c0 4.5 6 11 6 11s6-6.5 6-11a6 6 0 0 0-6-6zm0 8.5A2.5 2.5 0 1 1 6 3.5a2.5 2.5 0 0 1 0 5z" fill="#f7941d"/></svg></div>
  <p class="abs footer-text" style="left:266px;top:37px">Morvelink Dating<br>Contact | Morvelink | Dating Easy</p>
  <div class="abs footer-icon" style="left:512px;top:40px"><svg width="13" height="13" viewBox="0 0 16 16"><path d="M3.5 0.5l2.5 3-1.6 2a9 9 0 0 0 6.1 6.1l2-1.6 3 2.5-1.3 2.6C7.5 15 1 8.5.9 1.8z" fill="#f7941d"/></svg></div>
  <p class="abs footer-text" style="left:567px;top:49px">1 555 204 7310</p>
  <div class="abs footer-icon" style="left:701px;top:40px"><svg width="16" height="12" viewBox="0 0 18 13"><rect width="18" height="13" rx="1.5" fill="#f7941d"/><path d="M0.5 1.5l8.5 6 8.5-6" stroke="#ececec" stroke-width="1.5" fill="none"/></svg></div>
  <p class="abs footer-text" style="left:756px;top:47px">contact@morvelink.com</p>

  <p class="abs footer-links">Morvelink &nbsp;| &nbsp;About &nbsp;| &nbsp;Contact &nbsp;| &nbsp;Login &nbsp;| &nbsp;Members &nbsp;| &nbsp;Premium &nbsp;| &nbsp;Register &nbsp;| &nbsp;Search</p>
  <div class="abs footer-rule"></div>
  <p class="abs copyright">Copyrights © 2017, Morvelink. All rights reserved.</p>
  <span class="abs footer-social" style="left:897px;top:176px"></span>
  <span class="abs footer-social" style="left:936px;top:176px"></span>
  <span class="abs footer-social" style="left:975px;top:176px"></span>
</footer>
</body>
</html>
```